b2c portal. ZippyGrub. Attract diners and drinkers to restaurant/bar deals

aggregator site for restaurants and bars to promote their deals/discounts

1. we are an aggregator portal that lists all deals and discounts (Happy Hour, etc.) for restaurants and bars. the layout is similar to Kivo and RoamScout, without the ratings.
2. the target market is identical to Kivo and those searching for restaurants on RoamScout.
3. I have attached a file of a preliminary screenshot of a home page.

Target Market(s)

all guests of restaurants and bars

Number of Pages Required

4 page

Requirements
Must have
• a good story loop.
see Kivo, RoamScout, DashMeals
Should not have
• keep it simple

```html
<!DOCTYPE html>
<html lang="en">
<head>
<meta charset="utf-8">
<title>ZippyGrub – Find Restaurant Offers</title>
<link rel="stylesheet" href="https://fonts.googleapis.com/css2?family=Montserrat:ital,wght@0,400;0,500;0,600;0,700;0,800;1,400&display=swap">
<style>
:root{
  --orange:#c9652b;
  --orange-dark:#b4561f;
  --teal:#2b6c73;
  --panel:rgba(22,86,92,.88);
  --ink:#222;
  --muted:#555;
  --soft:#888;
  --line:#e4e4e4;
  --bg-soft:#f4f4f4;
  --white:#fff;
  --rate:#d93a2e;
}
*{box-sizing:border-box;margin:0;padding:0}
html,body{width:1200px;height:4138px;overflow:hidden}
body{font-family:'Montserrat',sans-serif;color:var(--ink);background:var(--white);position:relative}
.sprite{position:absolute;width:0;height:0}

/* Hero */
.hero{position:absolute;left:0;top:0;width:1200px;height:691px}
.hero-photo{position:absolute;inset:0;background:
  radial-gradient(ellipse at 50% 30%,rgba(120,70,35,.55),transparent 60%),
  linear-gradient(180deg,#3a2518 0%,#4b3020 35%,#2e2018 70%,#1f1812 100%)}
.nav{position:absolute;top:48px;left:145px;right:145px;height:40px;display:flex;align-items:center}
.nav a{color:var(--white);text-decoration:none;font-size:13px;margin-right:26px}
.nav a.active{border-bottom:2px solid var(--orange);padding-bottom:8px;margin-top:10px}
.brand{position:absolute;left:50%;transform:translateX(-50%);top:0;font-size:34px;font-weight:700;color:var(--orange);letter-spacing:.5px;line-height:40px}
.nav-right{margin-left:auto;display:flex;align-items:center}
.nav-right a{margin-right:22px}
.btn-sign{background:var(--orange);color:var(--white);font-size:13px;font-weight:700;padding:11px 20px;margin-right:12px}
.btn-login{border:2px solid var(--white);color:var(--white);font-size:13px;font-weight:700;padding:9px 24px}
.hero-title{position:absolute;top:222px;width:100%;text-align:center;color:var(--white);font-size:57px;font-weight:800}
.offer-types{position:absolute;top:334px;left:0;width:100%;display:flex;justify-content:center;gap:0}
.offer{width:110px;text-align:center;color:var(--white);font-size:13px}
.offer svg{display:block;margin:0 auto 10px;width:22px;height:22px}
.search-panel{position:absolute;left:162px;top:430px;width:874px;height:113px;background:var(--panel);padding:14px 24px}
.search-panel .col{position:absolute;top:14px;width:368px}
.search-panel .col.a{left:24px}
.search-panel .col.b{left:480px}
.search-panel label{display:block;color:var(--white);font-weight:600;font-size:16px;margin-bottom:12px}
.field{display:flex;height:40px}
.field span{flex:1;background:var(--white);font-size:13px;color:#666;padding:0 16px;line-height:40px}
.field b{width:50px;background:var(--orange);display:flex;align-items:center;justify-content:center}
.or{position:absolute;left:424px;top:60px;color:var(--white);font-weight:700;font-size:17px}
.dots{position:absolute;top:628px;width:100%;display:flex;justify-content:center;gap:6px}
.dots i{width:9px;height:9px;border-radius:50%;background:var(--white)}
.dots i.on{background:transparent;border:2px solid var(--white)}

/* Best businesses */
.best{position:absolute;top:691px;left:0;width:1200px;height:481px;background:var(--bg-soft)}
.section-title{position:absolute;width:100%;text-align:center;font-size:32px;font-weight:700;color:var(--ink)}
.best .section-title{top:80px}
.best-grid{position:absolute;top:163px;left:145px;display:flex;gap:10px}
.best-item{width:220px;text-align:center}
.photo{display:block}
.best-item .photo{height:200px}
.best-item h3{font-size:16px;font-weight:700;margin-top:18px;letter-spacing:.3px}

/* Collections */
.collections .section-title{top:1265px}
.cities{position:absolute;top:1340px;width:100%;text-align:center;font-size:14px;color:#333}
.cities span{margin:0 14px}
.cities em{font-style:normal;color:#999}
.card-grid{position:absolute;left:145px;display:grid;grid-template-columns:repeat(3,290px);column-gap:20px;row-gap:21px}
.coll-grid{top:1408px}
.coll-card{height:383px;background:var(--white);box-shadow:0 1px 5px rgba(0,0,0,.14)}
.coll-card .photo{height:217px}
.coll-card .body{padding:22px 29px}
.coll-card h4{font-size:17px;font-weight:700}
.addr{font-size:13px;color:var(--muted);margin-top:16px;display:flex;align-items:center;gap:5px}
.rating{display:flex;align-items:center;gap:2px;margin-top:14px;font-size:13px;color:var(--muted)}
.rating .count{margin-left:10px}
.opened{font-size:12px;color:var(--muted);margin-top:13px}
.btn-more{position:absolute;left:455px;width:290px;height:53px;background:var(--orange);color:var(--white);font-weight:700;font-size:16px;display:flex;align-items:center;justify-content:center;letter-spacing:.3px}
.divider{position:absolute;top:2393px;left:25px;right:25px;height:1px;background:var(--line)}

/* Reviews */
.reviews .section-title{top:2472px}
.rev-grid{top:2570px;row-gap:18px}
.rev-card{height:422px;background:var(--white);box-shadow:0 1px 5px rgba(0,0,0,.14);position:relative}
.rev-head{height:72px;display:flex;align-items:center;padding:0 10px;position:relative}
.avatar{width:50px;height:50px;border-radius:50%;background:#e2e2e2;display:flex;align-items:flex-end;justify-content:center;overflow:hidden}
.who{margin-left:27px}
.who b{display:block;font-size:16px}
.who small{font-size:11px;color:var(--soft)}
.ago{position:absolute;right:12px;top:18px;font-size:12px;color:#444}
.rev-card .photo{height:148px}
.rev-body{padding:24px 28px 0}
.rev-stars{display:flex;align-items:center;gap:3px;font-size:13px;color:var(--muted)}
.rev-stars .count{margin-left:4px}
.quote{font-size:13px;font-style:italic;color:var(--muted);line-height:20px;margin-top:18px}
.rev-foot{position:absolute;left:12px;right:12px;bottom:12px;display:flex;gap:14px}
.rev-foot .award{margin-left:auto}

/* Footer */
.footer{position:absolute;top:3638px;left:0;width:1200px;height:500px;background:var(--bg-soft)}
.foot-col{position:absolute;top:70px}
.foot-col h5{font-size:19px;font-weight:700;color:var(--teal);margin-bottom:18px}
.foot-col a{display:block;font-size:13px;color:#444;text-decoration:none;line-height:30.5px}
.foot-bottom{position:absolute;top:401px;left:0;width:100%;border-top:1px solid #ddd;text-align:center;padding-top:40px;font-size:13px;color:#444}
</style>
</head>
<body>

<svg class="sprite" aria-hidden="true">
  <defs>
    <symbol id="star" viewBox="0 0 24 24"><path d="M12 2l2.9 6.6 7.1.6-5.4 4.7 1.6 7-6.2-3.7-6.2 3.7 1.6-7L2 9.2l7.1-.6z"/></symbol>
    <symbol id="pin" viewBox="0 0 24 24"><path d="M12 2a7 7 0 0 0-7 7c0 5 7 13 7 13s7-8 7-13a7 7 0 0 0-7-7zm0 9.5a2.5 2.5 0 1 1 0-5 2.5 2.5 0 0 1 0 5z"/></symbol>
    <symbol id="search" viewBox="0 0 24 24"><circle cx="10" cy="10" r="6.5" fill="none" stroke="#fff" stroke-width="3"/><path d="M15 15l6 6" stroke="#fff" stroke-width="3" stroke-linecap="round"/></symbol>
    <symbol id="rate" viewBox="0 0 20 20"><rect width="20" height="20" rx="2" fill="#d93a2e"/><path fill="#fff" d="M10 3.5l1.9 4.2 4.6.4-3.5 3 1.1 4.5-4.1-2.4-4.1 2.4 1.1-4.5-3.5-3 4.6-.4z"/></symbol>
    <symbol id="ic-bulb" viewBox="0 0 20 20"><circle cx="10" cy="10" r="8.5" fill="none" stroke="#999" stroke-width="1.3"/><path d="M10 5a3 3 0 0 0-1.6 5.5V12h3.2v-1.5A3 3 0 0 0 10 5zM8.6 13.5h2.8" fill="none" stroke="#999" stroke-width="1.2"/></symbol>
    <symbol id="ic-smile" viewBox="0 0 20 20"><circle cx="10" cy="10" r="8.5" fill="none" stroke="#999" stroke-width="1.3"/><circle cx="7.3" cy="8" r="1" fill="#999"/><circle cx="12.7" cy="8" r="1" fill="#999"/><path d="M6.5 11.5q3.5 3.5 7 0" fill="none" stroke="#999" stroke-width="1.3"/></symbol>
    <symbol id="ic-cool" viewBox="0 0 20 20"><circle cx="10" cy="10" r="8.5" fill="none" stroke="#999" stroke-width="1.3"/><rect x="4.5" y="7" width="4.5" height="2.8" rx="1" fill="#999"/><rect x="11" y="7" width="4.5" height="2.8" rx="1" fill="#999"/><path d="M7 13h6" stroke="#999" stroke-width="1.3"/></symbol>
    <symbol id="ic-award" viewBox="0 0 20 20"><circle cx="10" cy="8" r="5.5" fill="none" stroke="#999" stroke-width="1.4"/><path d="M7 12.5L6 18l4-2 4 2-1-5.5" fill="none" stroke="#999" stroke-width="1.4"/></symbol>
    <symbol id="person" viewBox="0 0 50 50"><circle cx="25" cy="20" r="9" fill="#c4c4c4"/><path d="M8 50a17 15 0 0 1 34 0z" fill="#c4c4c4"/></symbol>
  </defs>
</svg>

<!-- Hero -->
<header class="hero">
  <div class="hero-photo" role="img" aria-label="Warm-lit restaurant interior with wooden tables and hanging lamps"></div>
  <nav class="nav">
    <a class="active" href="#">Vacation Rentals</a>
    <a href="#">Things to Do</a>
    <a href="#">Restaurants</a>
    <div class="brand">ZippyGrub</div>
    <div class="nav-right">
      <a href="#">Write a review</a>
      <span class="btn-sign">SIGN IN</span>
      <span class="btn-login">LOGIN</span>
    </div>
  </nav>
  <h1 class="hero-title">Find Restaurant Offers</h1>
  <div class="offer-types">
    <div class="offer"><svg viewBox="0 0 24 24"><circle cx="12" cy="12" r="9" fill="none" stroke="#fff" stroke-width="2.4"/><path d="M12 7v5l3 2" fill="none" stroke="#fff" stroke-width="2.2"/></svg>Happy Tour</div>
    <div class="offer"><svg viewBox="0 0 24 24"><path d="M3 4h8l10 10-7 7L4 11z" fill="#fff"/><circle cx="7.5" cy="8" r="1.6" fill="#3a2518"/></svg>Daily Deals</div>
    <div class="offer" style="width:130px"><svg viewBox="0 0 24 24"><rect x="3" y="5" width="18" height="16" rx="1.5" fill="none" stroke="#fff" stroke-width="2"/><path d="M3 10h18M8 2v5M16 2v5" stroke="#fff" stroke-width="2"/></svg>Special Events</div>
    <div class="offer"><svg viewBox="0 0 24 24"><path d="M2 6h12v10H2zM14 9h4l4 4v3h-8z" fill="#fff"/><circle cx="6" cy="18" r="2.2" fill="#fff"/><circle cx="18" cy="18" r="2.2" fill="#fff"/></svg>Delivery</div>
    <div class="offer"><svg viewBox="0 0 24 24"><path fill="#fff" d="M12 1l2.6 2.3 3.4-.6 1 3.3 3.2 1.4-.9 3.4L23 13.6l-2.4 2.5.3 3.4-3.4.6-1.8 3-3.2-1.3-3.2 1.3-1.8-3-3.4-.6.3-3.4L1 13.6l1.7-2.8L1.8 7.4 5 6l1-3.3 3.4.6z"/></svg>Discount</div>
  </div>
  <form class="search-panel">
    <div class="col a"><label>Restaurant Locations</label><div class="field"><span>Where to?</span><b><svg width="20" height="20"><use href="#search"/></svg></b></div></div>
    <div class="or">OR</div>
    <div class="col b"><label>Restaurant Locations</label><div class="field"><span>Where to?</span><b><svg width="20" height="20"><use href="#search"/></svg></b></div></div>
  </form>
  <div class="dots"><i></i><i></i><i class="on"></i><i></i><i></i></div>
</header>

<!-- Best businesses -->
<section class="best">
  <h2 class="section-title">Find the Best Businesses in Town</h2>
  <div class="best-grid">
    <div class="best-item"><div class="photo" role="img" aria-label="Plated dish with wine glasses on a table" style="background:linear-gradient(135deg,#e9a24a,#8a4a25 55%,#d9d2c8)"></div><h3>LOREM IPSUM</h3></div>
    <div class="best-item"><div class="photo" role="img" aria-label="Friends sharing a meal at a restaurant" style="background:linear-gradient(135deg,#6b4a35,#b98a68 50%,#4b352a)"></div><h3>TEMPOR INCIDID</h3></div>
    <div class="best-item"><div class="photo" role="img" aria-label="Colourful plates of food on a table" style="background:linear-gradient(135deg,#a9a39a,#d98b3a 50%,#7a8a3e)"></div><h3>EIUSMOD</h3></div>
    <div class="best-item"><div class="photo" role="img" aria-label="Group laughing over dinner" style="background:linear-gradient(135deg,#5a3d30,#b0785a 50%,#3e2d26)"></div><h3>DUIS AUTE</h3></div>
  </div>
</section>

<!-- Collections -->
<section class="collections">
  <h2 class="section-title">Collections</h2>
  <div class="cities"><span>New York</span><em>|</em><span>San Jose</span><em>|</em><span>Los Angeles</span><em>|</em><span>Chicago</span><em>|</em><span>Palo Alto</span><em>|</em><span>Oakland</span></div>
  <div class="card-grid coll-grid">
    <article class="coll-card"><div class="photo" role="img" aria-label="Diners around a table" style="background:linear-gradient(135deg,#5c5a4a,#a58a6c 50%,#3d3a32)"></div><div class="body"><h4>Minim veniam</h4><p class="addr"><svg width="11" height="12" fill="#2b6c73"><use href="#pin"/></svg>123,Sed ut perspiciatis unomnis</p><div class="rating"><svg width="16" height="16" fill="#c9652b"><use href="#star"/></svg><svg width="16" height="16" fill="#c9652b"><use href="#star"/></svg><svg width="16" height="16" fill="#c9652b"><use href="#star"/></svg><svg width="16" height="16" fill="#c9652b"><use href="#star"/></svg><svg width="16" height="16" fill="#c9652b"><use href="#star"/></svg><span class="count">5 Reviews</span></div><p class="opened">Opened 8 weeks ago</p></div></article>
    <article class="coll-card"><div class="photo" role="img" aria-label="Waiter serving plated dishes" style="background:linear-gradient(135deg,#2e2a28,#7a5a48 50%,#c9c2b8)"></div><div class="body"><h4>Ullamco laboris</h4><p class="addr"><svg width="11" height="12" fill="#2b6c73"><use href="#pin"/></svg>123,Sed ut perspiciatis unomnis</p><div class="rating"><svg width="16" height="16" fill="#c9652b"><use href="#star"/></svg><svg width="16" height="16" fill="#c9652b"><use href="#star"/></svg><svg width="16" height="16" fill="#c9652b"><use href="#star"/></svg><svg width="16" height="16" fill="#c9652b"><use href="#star"/></svg><svg width="16" height="16" fill="#c9652b"><use href="#star"/></svg><span class="count">5 Reviews</span></div><p class="opened">Opened 8 weeks ago</p></div></article>
    <article class="coll-card"><div class="photo" role="img" aria-label="Gourmet dish on a white plate" style="background:linear-gradient(135deg,#3a4048,#e0dcd4 50%,#d6a23a)"></div><div class="body"><h4>Nam libero tempore</h4><p class="addr"><svg width="11" height="12" fill="#2b6c73"><use href="#pin"/></svg>123,Sed ut perspiciatis unomnis</p><div class="rating"><svg width="16" height="16" fill="#c9652b"><use href="#star"/></svg><svg width="16" height="16" fill="#c9652b"><use href="#star"/></svg><svg width="16" height="16" fill="#c9652b"><use href="#star"/></svg><svg width="16" height="16" fill="#c9652b"><use href="#star"/></svg><svg width="16" height="16" fill="#c9652b"><use href="#star"/></svg><span class="count">5 Reviews</span></div><p class="opened">Opened 8 weeks ago</p></div></article>
    <article class="coll-card"><div class="photo" role="img" aria-label="Salad bowls on a wooden table seen from above" style="background:linear-gradient(135deg,#7a5230,#a9b36a 50%,#e8e2d6)"></div><div class="body"><h4>Minim veniam</h4><p class="addr"><svg width="11" height="12" fill="#2b6c73"><use href="#pin"/></svg>123,Sed ut perspiciatis unomnis</p><div class="rating"><svg width="16" height="16" fill="#c9652b"><use href="#star"/></svg><svg width="16" height="16" fill="#c9652b"><use href="#star"/></svg><svg width="16" height="16" fill="#c9652b"><use href="#star"/></svg><svg width="16" height="16" fill="#c9652b"><use href="#star"/></svg><svg width="16" height="16" fill="#c9652b"><use href="#star"/></svg><span class="count">5 Reviews</span></div><p class="opened">Opened 8 weeks ago</p></div></article>
    <article class="coll-card"><div class="photo" role="img" aria-label="Empty restaurant with wooden bar" style="background:linear-gradient(135deg,#2a2420,#8a5a32 50%,#3a2e26)"></div><div class="body"><h4>Ullamco laboris</h4><p class="addr"><svg width="11" height="12" fill="#2b6c73"><use href="#pin"/></svg>123,Sed ut perspiciatis unomnis</p><div class="rating"><svg width="16" height="16" fill="#c9652b"><use href="#star"/></svg><svg width="16" height="16" fill="#c9652b"><use href="#star"/></svg><svg width="16" height="16" fill="#c9652b"><use href="#star"/></svg><svg width="16" height="16" fill="#c9652b"><use href="#star"/></svg><svg width="16" height="16" fill="#c9652b"><use href="#star"/></svg><span class="count">5 Reviews</span></div><p class="opened">Opened 8 weeks ago</p></div></article>
    <article class="coll-card"><div class="photo" role="img" aria-label="Chef garnishing grilled meat" style="background:linear-gradient(135deg,#cfc8c0,#6a3a26 50%,#d2a046)"></div><div class="body"><h4>Nam libero tempore</h4><p class="addr"><svg width="11" height="12" fill="#2b6c73"><use href="#pin"/></svg>123,Sed ut perspiciatis unomnis</p><div class="rating"><svg width="16" height="16" fill="#c9652b"><use href="#star"/></svg><svg width="16" height="16" fill="#c9652b"><use href="#star"/></svg><svg width="16" height="16" fill="#c9652b"><use href="#star"/></svg><svg width="16" height="16" fill="#c9652b"><use href="#star"/></svg><svg width="16" height="16" fill="#c9652b"><use href="#star"/></svg><span class="count">5 Reviews</span></div><p class="opened">Opened 8 weeks ago</p></div></article>
  </div>
  <div class="btn-more" style="top:2252px">SEE MORE COLLECTIONS</div>
</section>

<div class="divider"></div>

<!-- Reviews -->
<section class="reviews">
  <h2 class="section-title">Customer Reviews</h2>
  <div class="card-grid rev-grid">
    <article class="rev-card"><div class="rev-head"><div class="avatar"><svg width="50" height="50"><use href="#person"/></svg></div><div class="who"><b>Rachana H.</b><small>Added 1 photo</small></div><span class="ago">8 weeks ago</span></div><div class="photo" role="img" aria-label="Friends laughing at a restaurant table" style="background:linear-gradient(135deg,#4a3a2e,#a87a5a 50%,#2e2620)"></div><div class="rev-body"><div class="rev-stars"><svg width="19" height="19"><use href="#rate"/></svg><svg width="19" height="19"><use href="#rate"/></svg><svg width="19" height="19"><use href="#rate"/></svg><svg width="19" height="19"><use href="#rate"/></svg><svg width="19" height="19"><use href="#rate"/></svg><span class="count">5 Reviews</span></div><p class="quote">"At vero eos et accusamus et iusto dio dignissimos ducimus qui blan ditiis praesentium voluptatummil iquunt m et dolorum fuga.</p></div><div class="rev-foot"><svg width="20" height="20"><use href="#ic-bulb"/></svg><svg width="20" height="20"><use href="#ic-smile"/></svg><svg width="20" height="20"><use href="#ic-cool"/></svg><svg class="award" width="20" height="20"><use href="#ic-award"/></svg></div></article>
    <article class="rev-card"><div class="rev-head"><div class="avatar"><svg width="50" height="50"><use href="#person"/></svg></div><div class="who"><b>Johnys H.</b><small>Added 1 photo</small></div><span class="ago">8 weeks ago</span></div><div class="photo" role="img" aria-label="Diners sharing dishes" style="background:linear-gradient(135deg,#5a4a3e,#b89878 50%,#6a5040)"></div><div class="rev-body"><div class="rev-stars"><svg width="19" height="19"><use href="#rate"/></svg><svg width="19" height="19"><use href="#rate"/></svg><svg width="19" height="19"><use href="#rate"/></svg><svg width="19" height="19"><use href="#rate"/></svg><svg width="19" height="19"><use href="#rate"/></svg><span class="count">5 Reviews</span></div><p class="quote">"At vero eos et accusamus et iusto dio dignissimos ducimus qui blan ditiis praesentium voluptatummil iquunt m et dolorum fuga.</p></div><div class="rev-foot"><svg width="20" height="20"><use href="#ic-bulb"/></svg><svg width="20" height="20"><use href="#ic-smile"/></svg><svg width="20" height="20"><use href="#ic-cool"/></svg><svg class="award" width="20" height="20"><use href="#ic-award"/></svg></div></article>
    <article class="rev-card"><div class="rev-head"><div class="avatar"><svg width="50" height="50"><use href="#person"/></svg></div><div class="who"><b>Doe Prgah H.</b><small>Added 1 photo</small></div><span class="ago">8 weeks ago</span></div><div class="photo" role="img" aria-label="Group dining together" style="background:linear-gradient(135deg,#6a5a4a,#c8a888 50%,#4a3a30)"></div><div class="rev-body"><div class="rev-stars"><svg width="19" height="19"><use href="#rate"/></svg><svg width="19" height="19"><use href="#rate"/></svg><svg width="19" height="19"><use href="#rate"/></svg><svg width="19" height="19"><use href="#rate"/></svg><svg width="19" height="19"><use href="#rate"/></svg><span class="count">5 Reviews</span></div><p class="quote">"At vero eos et accusamus et iusto dio dignissimos ducimus qui blan ditiis praesentium voluptatummil iquunt m et dolorum fuga.</p></div><div class="rev-foot"><svg width="20" height="20"><use href="#ic-bulb"/></svg><svg width="20" height="20"><use href="#ic-smile"/></svg><svg width="20" height="20"><use href="#ic-cool"/></svg><svg class="award" width="20" height="20"><use href="#ic-award"/></svg></div></article>
    <article class="rev-card"><div class="rev-head"><div class="avatar"><svg width="50" height="50"><use href="#person"/></svg></div><div class="who"><b>John Doe H.</b><small>Added 1 photo</small></div><span class="ago">8 weeks ago</span></div><div class="photo" role="img" aria-label="Friends at a dinner party" style="background:linear-gradient(135deg,#3e2e26,#9a6a4a 50%,#5a4030)"></div><div class="rev-body"><div class="rev-stars"><svg width="19" height="19"><use href="#rate"/></svg><svg width="19" height="19"><use href="#rate"/></svg><svg width="19" height="19"><use href="#rate"/></svg><svg width="19" height="19"><use href="#rate"/></svg><svg width="19" height="19"><use href="#rate"/></svg><span class="count">5 Reviews</span></div><p class="quote">"At vero eos et accusamus et iusto dio dignissimos ducimus qui blan ditiis praesentium voluptatummil iquunt m et dolorum fuga.</p></div><div class="rev-foot"><svg width="20" height="20"><use href="#ic-bulb"/></svg><svg width="20" height="20"><use href="#ic-smile"/></svg><svg width="20" height="20"><use href="#ic-cool"/></svg><svg class="award" width="20" height="20"><use href="#ic-award"/></svg></div></article>
    <article class="rev-card"><div class="rev-head"><div class="avatar"><svg width="50" height="50"><use href="#person"/></svg></div><div class="who"><b>Smitha H.</b><small>Added 1 photo</small></div><span class="ago">8 weeks ago</span></div><div class="photo" role="img" aria-label="Guest enjoying a meal in a dim restaurant" style="background:linear-gradient(135deg,#2a2a34,#6a4a3a 50%,#2e2a2a)"></div><div class="rev-body"><div class="rev-stars"><svg width="19" height="19"><use href="#rate"/></svg><svg width="19" height="19"><use href="#rate"/></svg><svg width="19" height="19"><use href="#rate"/></svg><svg width="19" height="19"><use href="#rate"/></svg><svg width="19" height="19"><use href="#rate"/></svg><span class="count">5 Reviews</span></div><p class="quote">"At vero eos et accusamus et iusto dio dignissimos ducimus qui blan ditiis praesentium voluptatummil iquunt m et dolorum fuga.</p></div><div class="rev-foot"><svg width="20" height="20"><use href="#ic-bulb"/></svg><svg width="20" height="20"><use href="#ic-smile"/></svg><svg width="20" height="20"><use href="#ic-cool"/></svg><svg class="award" width="20" height="20"><use href="#ic-award"/></svg></div></article>
    <article class="rev-card"><div class="rev-head"><div class="avatar"><svg width="50" height="50"><use href="#person"/></svg></div><div class="who"><b>Rachana H.</b><small>Added 1 photo</small></div><span class="ago">8 weeks ago</span></div><div class="photo" role="img" aria-label="Guest with a drink on a terrace" style="background:linear-gradient(135deg,#6a7a8a,#a86a5a 50%,#c8b8a8)"></div><div class="rev-body"><div class="rev-stars"><svg width="19" height="19"><use href="#rate"/></svg><svg width="19" height="19"><use href="#rate"/></svg><svg width="19" height="19"><use href="#rate"/></svg><svg width="19" height="19"><use href="#rate"/></svg><svg width="19" height="19"><use href="#rate"/></svg><span class="count">5 Reviews</span></div><p class="quote">"At vero eos et accusamus et iusto dio dignissimos ducimus qui blan ditiis praesentium voluptatummil iquunt m et dolorum fuga.</p></div><div class="rev-foot"><svg width="20" height="20"><use href="#ic-bulb"/></svg><svg width="20" height="20"><use href="#ic-smile"/></svg><svg width="20" height="20"><use href="#ic-cool"/></svg><svg class="award" width="20" height="20"><use href="#ic-award"/></svg></div></article>
  </div>
  <div class="btn-more" style="top:3496px">SEE MORE RATINGS</div>
</section>

<!-- Footer -->
<footer class="footer">
  <div class="foot-col" style="left:145px"><h5>ABOUT</h5><a href="#">About Us</a><a href="#">Careers</a><a href="#">Press</a><a href="#">Investor Relations</a><a href="#">Content Guidelines</a><a href="#">Terms of Service</a><a href="#">Privacy Policy</a></div>
  <div class="foot-col" style="left:397px"><h5>DISCOVER</h5><a href="#">Project Cost Guides</a><a href="#">Collections</a><a href="#">Talk</a><a href="#">Events</a><a href="#">Support</a><a href="#">Developers</a><a href="#">Ad Choices</a></div>
  <div class="foot-col" style="left:650px"><h5>FOR BUSINESS</h5><a href="#">Claim your Business Page</a><a href="#">Advertise</a><a href="#">Restaurant Owners</a><a href="#">Table Management</a><a href="#">Business Success Stories</a><a href="#">Business Support</a><a href="#">Blog for Business</a></div>
  <div class="foot-col" style="left:944px"><h5>LINKS</h5><a href="#">Vacation Rentals</a><a href="#">Things to Do</a><a href="#">Restaurants</a><a href="#">Write a review</a><a href="#">Travel Forums</a><a href="#">More</a></div>
  <div class="foot-bottom">Copyright © 2020 ZippyGrub.All Rights Reserved &nbsp;|&nbsp; Privacy Policy &nbsp;|&nbsp; Terms and Use</div>
</footer>

</body>
</html>
```